Bluestone Nine LLC Flyer Design

Marketing Materials for Real Estate Company. This flyer will be used to promote the company throughout the Commercial Real Estate business in the United States. The team has been together for 15 years. We are the middle guys between the Tenant, Broker, and the Owner. In the case of working with a Franchisor, we will be their Plug and Play leasing arm that will assist their new Franchisee's with their site selection, lease negotiations, design and construction management.

Target Market(s)

Real Estate Owners, Franchisor's, and Brokers

Font styles to use
Serif

Colors

Designer to choose colors to be used in the design.

Requirements
Must have
• The flyer must have......
• 1. The Best Leasing Machine On The Planet
• 2. Over the past 15 years our group has completed 4,492 lease transactions resulting in leasing 17,803,114 square feet in shopping centers across the United States.
• 3. Plug and Play Leasing Specialists. We handle the details between when the broker shows up with the space and the tenant and completing the lease negotiations, legal negotiations and documentation, and construction management to Certificate of Occupancy.
• 4. For Information Call Colette Warrick at 303-555-0142 or Noelle Hadley at 303-555-0178.
Nice to have
• National Tenants the we have completed transactions with....
• Markwell, Fernvale Grocers, Harbor Pantry, Vesko, Pell, QR Outlet, Burrovia, Grillorama, Salsa Hut, Brewmoor, Summit Gymworks, ParcelQuik, Roadgrip, NPQ, Medlowe, K&Z, Union Harbor Bank, Hen Haven, Lotus Wok, Furvio, Dal-Bazaar, Meadowly, and Orbit Theatres

```html
<!DOCTYPE html>
<html lang="en">
<head>
<meta charset="utf-8">
<title>Bluestone Nine LLC Flyer</title>
<link href="https://fonts.googleapis.com/css2?family=Source+Sans+3:wght@400;600;700&display=swap" rel="stylesheet">
<style>
  :root {
    --page-bg: #8a8a8a;
    --flyer-black: #050505;
    --lime: #a6bf5c;
    --olive-band: #4a5037;
    --olive-line: #9aae55;
    --white: #ffffff;
    --soft-white: #e9e9e4;
    --tenant-grey: #cfcfc8;
    --photo-top: #141614;
    --photo-mid: #6f7a62;
    --photo-light: #a9b497;
  }
  * { box-sizing: border-box; margin: 0; padding: 0; }
  html, body { width: 1200px; height: 1200px; overflow: hidden; }
  body {
    background: var(--page-bg);
    font-family: "Source Sans 3", "Myriad Pro", sans-serif;
    color: var(--white);
    position: relative;
  }
  .flyer {
    position: absolute;
    left: 190px; top: 70px;
    width: 820px; height: 1060px;
    background: var(--flyer-black);
    overflow: hidden;
  }
  .hero-photo {
    position: absolute; left: 0; top: 0;
    width: 820px; height: 690px;
    background:
      linear-gradient(180deg, rgba(5,5,5,0.95) 0%, rgba(5,5,5,0.5) 12%, rgba(0,0,0,0) 30%, rgba(0,0,0,0) 62%, rgba(5,5,5,0.85) 85%, var(--flyer-black) 100%),
      linear-gradient(180deg, var(--photo-top) 0%, var(--photo-mid) 35%, var(--photo-light) 52%, #5d6a55 66%, #2a2e28 80%);
  }
  .headline {
    position: absolute; left: 50px; top: 65px;
    font-size: 31px; font-weight: 400; line-height: 1.12;
    color: var(--white);
  }
  .headline-rule {
    position: absolute; left: 52px; top: 142px;
    width: 320px; height: 2px;
    background: var(--olive-line);
  }
  .headline-stats {
    position: absolute; left: 60px; top: 146px;
    font-size: 13.5px; color: var(--soft-white);
  }
  .brand-banner {
    position: absolute; left: 386px; top: 62px;
    width: 434px; height: 110px;
  }
  .brand-name {
    position: absolute; left: 420px; top: 88px;
    width: 380px; text-align: center;
    font-size: 33px; font-weight: 600; letter-spacing: 1.5px;
    color: var(--white);
  }
  .track-record {
    position: absolute; left: 60px; top: 520px;
    width: 700px; text-align: center;
    font-size: 24px; line-height: 1.35; color: var(--white);
  }
  .services-band {
    position: absolute; left: 70px; top: 640px;
    width: 690px; height: 100px;
    background: var(--olive-band);
    display: flex; align-items: center; justify-content: center;
    padding: 0 24px;
    text-align: center; font-size: 14.5px; line-height: 1.4;
    color: var(--soft-white);
  }
  .tenants-heading {
    position: absolute; left: 0; top: 780px; width: 820px;
    text-align: center; font-size: 14px; letter-spacing: 3.2px;
    color: var(--white);
  }
  .tenant-row {
    position: absolute; left: 60px; width: 720px;
    display: grid; align-items: center; column-gap: 6px;
  }
  .tenant-row.first { top: 820px; grid-template-columns: repeat(12, 1fr); }
  .tenant-row.second { top: 875px; grid-template-columns: repeat(11, 1fr); left: 70px; width: 690px; }
  .tenant {
    font-size: 11px; font-weight: 600; line-height: 1.15;
    text-align: center; color: var(--tenant-grey);
  }
  .contact {
    position: absolute; left: 0; top: 950px; width: 820px;
    text-align: center;
  }
  .contact-label { font-size: 15px; color: var(--white); }
  .contact-line { font-size: 17px; margin-top: 4px; color: var(--white); }
  .contact-line strong { font-weight: 700; }
  .contact-line .sep { margin: 0 10px; }
</style>
</head>
<body>
  <div class="flyer">
    <div class="hero-photo" role="img" aria-label="Silhouetted business people meeting in front of tall office windows overlooking a hazy city skyline"></div>

    <h1 class="headline">The Best Leasing Machine<br>On The Planet</h1>
    <div class="headline-rule"></div>
    <p class="headline-stats">4,492 lease transactions | 17,803,114 square feet</p>

    <svg class="brand-banner" viewBox="0 0 434 110" aria-hidden="true">
      <polygon points="36,18 434,0 434,82 0,110" fill="var(--lime)"/>
    </svg>
    <div class="brand-name">Bluestone Nine LLC</div>

    <p class="track-record">Over the past 15 years our group has completed 4,492<br>lease transactions resulting in leasing 17,803,114 sq.ft.<br>in shopping centers across the United States.</p>

    <p class="services-band">Plug and Play Leasing Specialists. We handle the details between when the broker shows up with the space and the tenant and completing the lease negotiations, legal negotiations and documentation, and construction management to Certificate of Occupancy.</p>

    <p class="tenants-heading">National Tenants the we have completed transactions with....</p>

    <div class="tenant-row first">
      <span class="tenant">Medlowe</span>
      <span class="tenant">Markwell</span>
      <span class="tenant">Fernvale Grocers</span>
      <span class="tenant">Harbor Pantry</span>
      <span class="tenant">Vesko</span>
      <span class="tenant">Hen Haven</span>
      <span class="tenant">Lotus Wok</span>
      <span class="tenant">Furvio</span>
      <span class="tenant">Meadowly</span>
      <span class="tenant">Orbit Theatres</span>
      <span class="tenant">K&amp;Z</span>
      <span class="tenant">Roadgrip</span>
    </div>
    <div class="tenant-row second">
      <span class="tenant">Union Harbor Bank</span>
      <span class="tenant">Brewmoor</span>
      <span class="tenant">Salsa Hut</span>
      <span class="tenant">Grillorama</span>
      <span class="tenant">Pell</span>
      <span class="tenant">Burrovia</span>
      <span class="tenant">Dal-Bazaar</span>
      <span class="tenant">NPQ</span>
      <span class="tenant">Summit Gymworks</span>
      <span class="tenant">ParcelQuik</span>
      <span class="tenant">QR Outlet</span>
    </div>

    <div class="contact">
      <p class="contact-label">For Information Call</p>
      <p class="contact-line"><strong>Colette Warrick</strong> at 303-555-0142<span class="sep">or</span><strong>Noelle Hadley</strong> at 303-555-0178</p>
    </div>
  </div>
</body>
</html>
```